Labels for probiotic care products as Body Cream, Shower gel, Hand soap, ....

We are a starting a business in Flanders Belgium. We are looking for a label for care products, based on probiotics or good bacterie. We are looking for a fresh design that attracts people who wants a good product, based on naturally components. The products make that the microflora of the skin becomes and remains natural. The label must we be adaptive on bottles of 15 cm height to 8 cm height and a width of 4,5 cm. The brand name is KOVA REMU (beautiful skin in Hawaiian) or maybe just KOVA.

Industry/Entity Type

Business

Colors

Designer to choose colors to be used in the design.

Requirements
Must have
• somewhere the text "Probiotic Skin Care"
• I also have to tell that the bottles are white.
Nice to have
• I uploaded the 9 existing labels, but I want a totally new one, because the labels of our cleaning products are the same. I also uploaded a mood bord of labels I like.

```html
<!DOCTYPE html>
<html lang="en">
<head>
<meta charset="utf-8">
<title>KOVA REMU – Skin Repair Label</title>
<link rel="stylesheet" href="https://fonts.googleapis.com/css2?family=Josefin+Sans:wght@200;300&family=Zilla+Slab:wght@500&display=swap">
<style>
  :root {
    --page: #ffffff;
    --navy: #2c3a52;
    --pattern-light: #eceff3;
    --pattern-mid: #dfe3ea;
    --orange: #f0632a;
    --white: #ffffff;
  }
  html, body {
    margin: 0;
    padding: 0;
    overflow: hidden;
    background: var(--page);
  }
  .canvas {
    position: relative;
    width: 1175px;
    height: 1200px;
    background: var(--page);
    overflow: hidden;
  }
  .label {
    position: absolute;
    left: 392px;
    top: 103px;
    width: 392px;
    height: 987px;
  }
  .label-pattern {
    position: absolute;
    inset: 0;
    background: linear-gradient(180deg, var(--pattern-light), var(--pattern-mid) 50%, var(--pattern-light));
  }
  .title-panel {
    position: absolute;
    left: 54px;
    top: 242px;
    width: 290px;
    height: 411px;
    background: var(--navy);
    overflow: hidden;
  }
  .title-frame {
    position: absolute;
    left: 16px;
    top: 22px;
    right: 13px;
    bottom: 16px;
    border: 1.5px solid var(--white);
  }
  .brand-mark {
    position: absolute;
    left: 0;
    right: 0;
    top: 50px;
    text-align: center;
    font-family: "Josefin Sans", sans-serif;
    font-weight: 300;
    font-size: 22px;
    letter-spacing: 4px;
    color: var(--orange);
  }
  .brand-mark .dot {
    display: inline-block;
    width: 10px;
    height: 10px;
    background: var(--orange);
    margin-right: 8px;
    vertical-align: 2px;
  }
  .product-type {
    position: absolute;
    left: 0;
    right: 0;
    top: 146px;
    text-align: center;
    font-family: "Josefin Sans", sans-serif;
    font-weight: 300;
    font-size: 31px;
    color: var(--white);
  }
  .brand-name {
    position: absolute;
    left: 0;
    right: 0;
    top: 196px;
    text-align: center;
    font-family: "Josefin Sans", sans-serif;
    font-weight: 200;
    font-size: 42px;
    line-height: 1;
    color: var(--white);
    white-space: nowrap;
  }
  .tagline {
    position: absolute;
    left: 0;
    right: 0;
    top: 332px;
    text-align: center;
    font-family: "Zilla Slab", serif;
    font-weight: 500;
    font-size: 20px;
    color: var(--white);
  }
</style>
</head>
<body>
  <div class="canvas">
    <div class="label">
      <div class="label-pattern" role="img" aria-label="Repeating navy line pattern of interlocking hexagonal cube outlines on white"></div>
      <div class="title-panel">
        <div class="title-frame"></div>
        <div class="brand-mark"><span class="dot"></span>KOVA</div>
        <div class="product-type">Skin Repair</div>
        <div class="brand-name">KOVA REMU</div>
        <div class="tagline">Probiotic Skin Care</div>
      </div>
    </div>
  </div>
</body>
</html>
```